Visitenkarten für Goldankauf
Zielgruppe
wir sind fokussiert auf den Goldankauf
Aufgabenstellung
es soll elegant aber auch bisschen auffällig sein. aber nichts verspieltes
es heißt die Brandts Wertkontor
logo habe ich nicht

```html
<!DOCTYPE html>
<html lang="de">
<head>
<meta charset="utf-8">
<title>Brandts Wertkontor – Visitenkarten</title>
<link rel="stylesheet" href="https://fonts.googleapis.com/css2?family=Noto+Serif:wght@400;700&display=swap">
<style>
:root{
  --gold:#debc7f;
  --ink:#111111;
  --paper:#ffffff;
  --canvas:#f2f2f2;
  --shadow:rgba(0,0,0,.45);
}
*{margin:0;padding:0;box-sizing:border-box}
html,body{width:1200px;height:2417px;overflow:hidden;background:var(--canvas)}
body{position:relative;font-family:"Noto Serif",Georgia,serif;color:var(--ink)}
.band{position:absolute}
.band--top{left:487px;top:0;width:713px;height:106px;background:var(--gold)}
.band--bottom{left:0;top:2309px;width:713px;height:108px;background:#000}

.card{position:absolute;width:392px;height:253px;background:var(--paper);box-shadow:3px 3px 4px var(--shadow);overflow:hidden}
.card--gold{background:var(--gold);color:var(--paper)}

/* front */
.lockup{position:absolute;left:0;right:0;top:92px;display:flex;justify-content:center;align-items:center;gap:12px}
.lockup__mark{width:34px;height:34px;background:var(--gold)}
.lockup__text{display:flex;flex-direction:column}
.lockup__name{font-weight:700;font-size:20px;line-height:22px;color:var(--gold);text-transform:uppercase;letter-spacing:.5px;border-bottom:1px solid var(--ink);padding-bottom:3px}
.lockup__tagline{font-size:6.5px;line-height:9px;color:var(--gold);margin-top:4px;letter-spacing:.3px}

/* back */
.name{position:absolute;font-weight:700;font-size:19px;line-height:22px}
.role{position:absolute;font-size:11.5px;line-height:14px}
.brand{position:absolute;display:flex;align-items:center;gap:6px;font-weight:700;font-size:11px;line-height:12px;text-transform:uppercase;color:var(--gold);letter-spacing:.3px}
.brand__mark{width:14px;height:14px;background:var(--gold)}
.card--gold .brand{color:var(--paper)}
.card--gold .brand__mark{background:var(--paper)}
.contact{position:absolute;font-size:8.4px;line-height:14.5px}
.contact p:first-child{margin-bottom:7.5px}
.contact b{font-weight:700}
.rule{position:absolute;height:2px;background:var(--ink)}
.card--gold .rule{background:var(--paper)}
.rule--thin{height:1px;background:var(--gold)}
.card--gold .rule--thin{background:var(--paper)}
.strip{position:absolute;background:var(--gold)}
.card--gold .strip{background:var(--paper)}

.centered{left:0;right:0;text-align:center}
.centered.brand{justify-content:center}
</style>
</head>
<body>
<div class="band band--top"></div>

<!-- fronts -->
<section class="card" style="left:195px;top:262px">
  <div class="lockup"><div class="lockup__mark"></div><div class="lockup__text"><span class="lockup__name">Brandts<br>Wertkontor</span><span class="lockup__tagline">Professionelle und faire Bewertung<br>Ihrer Schmuckstücke</span></div></div>
</section>
<section class="card" style="left:195px;top:538px">
  <div class="lockup"><div class="lockup__mark"></div><div class="lockup__text"><span class="lockup__name">Brandts<br>Wertkontor</span><span class="lockup__tagline">Professionelle und faire Bewertung<br>Ihrer Schmuckstücke</span></div></div>
</section>
<section class="card" style="left:195px;top:815px">
  <div class="lockup"><div class="lockup__mark"></div><div class="lockup__text"><span class="lockup__name">Brandts<br>Wertkontor</span><span class="lockup__tagline">Professionelle und faire Bewertung<br>Ihrer Schmuckstücke</span></div></div>
</section>
<section class="card" style="left:193px;top:1375px">
  <div class="lockup"><div class="lockup__mark"></div><div class="lockup__text"><span class="lockup__name">Brandts<br>Wertkontor</span><span class="lockup__tagline">Professionelle und faire Bewertung<br>Ihrer Schmuckstücke</span></div></div>
</section>
<section class="card" style="left:193px;top:1652px">
  <div class="lockup"><div class="lockup__mark"></div><div class="lockup__text"><span class="lockup__name">Brandts<br>Wertkontor</span><span class="lockup__tagline">Professionelle und faire Bewertung<br>Ihrer Schmuckstücke</span></div></div>
</section>
<section class="card" style="left:193px;top:1929px">
  <div class="lockup"><div class="lockup__mark"></div><div class="lockup__text"><span class="lockup__name">Brandts<br>Wertkontor</span><span class="lockup__tagline">Professionelle und faire Bewertung<br>Ihrer Schmuckstücke</span></div></div>
</section>

<!-- backs, white -->
<section class="card" style="left:620px;top:262px">
  <h2 class="name centered" style="top:36px">Konrad Brandt</h2>
  <p class="role centered" style="top:62px">Inhaber</p>
  <div class="rule" style="left:38px;width:114px;top:69px"></div>
  <div class="rule" style="left:242px;width:113px;top:69px"></div>
  <div class="brand centered" style="top:146px"><span class="brand__mark"></span>Brandts Wertkontor</div>
  <div class="contact centered" style="top:181px"><p><b>Brandts Wertkontor</b> • Kastanienweg 12 • 80469 München</p><p><b>Fon</b> 089 / 44012377 • <b>Mobil</b> 0171 / 5523104 • kontakt@wertkontor-muenchen.de<br>www.wertkontor-muenchen.de</p></div>
  <div class="strip" style="left:0;right:0;bottom:0;height:11px"></div>
</section>

<section class="card" style="left:620px;top:538px">
  <div class="strip" style="left:0;top:0;bottom:0;width:13px"></div>
  <h2 class="name" style="left:27px;top:26px">Konrad Brandt</h2>
  <p class="role" style="left:27px;top:52px">Inhaber</p>
  <div class="brand" style="left:240px;top:36px"><span class="brand__mark"></span>Brandts<br>Wertkontor</div>
  <div class="contact" style="left:27px;top:182px"><p><b>Brandts Wertkontor</b> • Kastanienweg 12 • 80469 München</p><p><b>Fon</b> 089 / 44012377 • <b>Mobil</b> 0171 / 5523104 • kontakt@wertkontor-muenchen.de<br>www.wertkontor-muenchen.de</p></div>
</section>

<section class="card" style="left:620px;top:815px">
  <div class="brand" style="left:27px;top:36px"><span class="brand__mark"></span>Brandts<br>Wertkontor</div>
  <h2 class="name" style="left:27px;top:121px">Konrad Brandt</h2>
  <p class="role" style="left:27px;top:147px">Inhaber</p>
  <div class="rule rule--thin" style="left:27px;width:318px;top:170px"></div>
  <div class="contact" style="left:27px;top:182px"><p><b>Brandts Wertkontor</b> • Kastanienweg 12 • 80469 München</p><p><b>Fon</b> 089 / 44012377 • <b>Mobil</b> 0171 / 5523104 • kontakt@wertkontor-muenchen.de<br>www.wertkontor-muenchen.de</p></div>
</section>

<!-- backs, gold -->
<section class="card card--gold" style="left:617px;top:1375px">
  <h2 class="name centered" style="top:36px">Konrad Brandt</h2>
  <p class="role centered" style="top:62px">Inhaber</p>
  <div class="rule" style="left:38px;width:114px;top:69px"></div>
  <div class="rule" style="left:242px;width:113px;top:69px"></div>
  <div class="brand centered" style="top:146px"><span class="brand__mark"></span>Brandts Wertkontor</div>
  <div class="contact centered" style="top:181px"><p><b>Brandts Wertkontor</b> • Kastanienweg 12 • 80469 München</p><p><b>Fon</b> 089 / 44012377 • <b>Mobil</b> 0171 / 5523104 • kontakt@wertkontor-muenchen.de<br>www.wertkontor-muenchen.de</p></div>
  <div class="strip" style="left:0;right:0;bottom:0;height:11px"></div>
</section>

<section class="card card--gold" style="left:617px;top:1652px">
  <div class="strip" style="left:0;top:0;bottom:0;width:13px"></div>
  <h2 class="name" style="left:27px;top:26px">Konrad Brandt</h2>
  <p class="role" style="left:27px;top:52px">Inhaber</p>
  <div class="brand" style="left:240px;top:36px"><span class="brand__mark"></span>Brandts<br>Wertkontor</div>
  <div class="contact" style="left:27px;top:182px"><p><b>Brandts Wertkontor</b> • Kastanienweg 12 • 80469 München</p><p><b>Fon</b> 089 / 44012377 • <b>Mobil</b> 0171 / 5523104 • kontakt@wertkontor-muenchen.de<br>www.wertkontor-muenchen.de</p></div>
</section>

<section class="card card--gold" style="left:617px;top:1929px">
  <div class="brand" style="left:27px;top:36px"><span class="brand__mark"></span>Brandts<br>Wertkontor</div>
  <h2 class="name" style="left:27px;top:121px">Konrad Brandt</h2>
  <p class="role" style="left:27px;top:147px">Inhaber</p>
  <div class="rule rule--thin" style="left:27px;width:318px;top:170px"></div>
  <div class="contact" style="left:27px;top:182px"><p><b>Brandts Wertkontor</b> • Kastanienweg 12 • 80469 München</p><p><b>Fon</b> 089 / 44012377 • <b>Mobil</b> 0171 / 5523104 • kontakt@wertkontor-muenchen.de<br>www.wertkontor-muenchen.de</p></div>
</section>

<div class="band band--bottom"></div>
</body>
</html>
```